LA's Newest HEMP Facial Oil and Body Oil Packaging Project

We need a packaging concept for a Hemp based facial oil and body oil. We need label design for the bottle and carton graphics. I am attaching a few reference photos. The target demographic is women between 17-35 year old. Products need to be able to stand out in crowded stores with clear calls to action.
1oz Dropper Bottle with Unit Carton - Hemp Facial Oil
4oz PET Bottle with Unit Carton - Hemp + Rose Facial Oil

```html
<!DOCTYPE html>
<html lang="en">
<head>
<meta charset="utf-8">
<title>Hemp Facial Oil Packaging</title>
<link rel="stylesheet" href="https://fonts.googleapis.com/css2?family=Raleway:wght@300;400&display=swap">
<style>
  :root {
    --bg: #ffffff;
    --petal-pink: #f2c6d6;
    --petal-light: #f8dde7;
    --petal-deep: #e58fb0;
    --band-red: #a3162a;
    --band-red-light: #c41e35;
    --band-red-dark: #7e0f1f;
    --bar-black: #1f1d1e;
    --type-light: #f7eef1;
    --type-dark: #2a2226;
    --font: "Raleway", sans-serif;
  }
  * { box-sizing: border-box; margin: 0; padding: 0; }
  html, body {
    width: 1200px; height: 969px; overflow: hidden;
    background: var(--bg); font-family: var(--font);
  }
  .canvas { position: relative; width: 1200px; height: 969px; }

  .panel { position: absolute; overflow: hidden; }
  .petal-field {
    position: absolute; inset: 0;
    background:
      radial-gradient(circle at 70% 15%, var(--petal-deep) 0, transparent 22%),
      radial-gradient(circle at 25% 85%, var(--petal-deep) 0, transparent 20%),
      radial-gradient(circle at 80% 80%, #ec9dbb 0, transparent 18%),
      linear-gradient(160deg, var(--petal-light), var(--petal-pink));
  }

  .red-band {
    position: absolute; left: 0; right: 0;
    background: linear-gradient(90deg, var(--band-red-dark), var(--band-red-light) 55%, var(--band-red));
    display: flex; flex-direction: column; align-items: center; justify-content: center;
  }
  .hemp-title {
    font-weight: 300; color: var(--type-light); line-height: 1;
    letter-spacing: 0.01em; white-space: nowrap; text-align: center;
  }
  .hemp-title.dark { color: var(--type-dark); }
  .black-bar {
    background: var(--bar-black); color: var(--type-light);
    font-weight: 400; text-align: center; letter-spacing: 0.08em;
  }
  .subline {
    color: var(--type-light); font-weight: 300; letter-spacing: 0.06em;
    text-align: center; white-space: nowrap;
  }

  /* 4oz rose carton */
  .carton-rose { left: 40px; top: 70px; width: 320px; height: 830px; }
  .carton-rose .red-band { top: 330px; height: 250px; }
  .carton-rose .hemp-title { font-size: 96px; }
  .carton-rose .black-bar { width: 100%; font-size: 22px; padding: 12px 0; margin-top: 12px; }
  .carton-rose .subline { font-size: 22px; margin-top: 14px; }

  /* 4oz PET bottle label */
  .label-pet { left: 380px; top: 290px; width: 240px; height: 390px; background: var(--petal-light); }
  .label-pet .red-band { top: 40px; height: 310px; }
  .label-pet .hemp-title { font-size: 68px; }
  .label-pet .black-bar { width: 80%; font-size: 18px; padding: 10px 0; margin-top: 20px; }
  .label-pet .subline { font-size: 17px; margin-top: 14px; }

  /* 1oz dropper carton */
  .carton-drop { left: 640px; top: 150px; width: 260px; height: 600px; }
  .carton-drop .red-band { top: 230px; height: 200px; justify-content: flex-start; padding-top: 30px; }
  .carton-drop .hemp-title { font-size: 78px; }
  .carton-drop .black-bar { position: absolute; left: 0; right: 0; bottom: 0; font-size: 18px; padding: 12px 0; }

  /* 1oz dropper label */
  .label-drop { left: 930px; top: 330px; width: 230px; height: 330px; }
  .label-drop .hemp-title { position: absolute; top: 140px; left: 0; width: 100%; font-size: 60px; }
  .label-drop .red-band { bottom: 0; height: 70px; }
  .label-drop .subline { font-size: 16px; }
</style>
</head>
<body>
<main class="canvas">

  <section class="panel carton-rose">
    <div class="petal-field" role="img" aria-label="Pink rose petals scattered over a soft pink background"></div>
    <div class="red-band">
      <h1 class="hemp-title">HEMP</h1>
      <p class="black-bar">WITH</p>
      <p class="subline">ROSE FACIAL OIL</p>
    </div>
  </section>

  <section class="panel label-pet">
    <div class="red-band">
      <h2 class="hemp-title">HEMP</h2>
      <p class="black-bar">WITH</p>
      <p class="subline">ROSE FACIAL OIL</p>
    </div>
  </section>

  <section class="panel carton-drop">
    <div class="petal-field" role="img" aria-label="Pink rose petals with a falling oil drop on a soft pink background"></div>
    <div class="red-band">
      <h2 class="hemp-title">HEMP</h2>
      <p class="black-bar">FACIAL OIL</p>
    </div>
  </section>

  <section class="panel label-drop">
    <div class="petal-field" role="img" aria-label="Pink rose petals on a light pink background"></div>
    <h2 class="hemp-title dark">HEMP</h2>
    <div class="red-band">
      <p class="subline">FACIAL OIL</p>
    </div>
  </section>

</main>
</body>
</html>
```